Beacon Lending and Capital. We provide MOSTLY residential home mortgages in Florida AND commercial loans for investment properties throughout the United states.
I would love to emulate so of the lender sites that are available on the internet but I would like to have the site as popular as possible for SEO purposes. Clients can already click the link to take them to the mortgage application where they can complete that and upload documents. If you could polish that up for me that would be great. I can also provide you with great detail on loan programs that are currently being offered. WE OFFER ALL MORTGAGE LENDING PRODUCTS. I would also like to add something in reference to the rate but I don't think it's legal to actually state or promise a rate for mortgage since they vary based on loan type, client and other criteria...

On the Beacon real estate site I would like to add a link or some way for clients to be able to put in credit card information to render services ...

Please let me know what you need from me

Thank you !!

Current link to site to improve and code

https://beaconlendingandcapital.example/

Industry/Entity Type

Residential and commmercial lending

Coding

Coded - Design and coding required

Number of Pages Required

2 page

Requirements
Must have
• Love to integrate Mortgage interest rates even if general
Nice to have
• Link to fill out mortgage application via Quillo MLO software

```html
<!DOCTYPE html>
<html lang="en">
<head>
<meta charset="utf-8">
<title>Beacon Lending and Capital</title>
<link href="https://fonts.googleapis.com/css2?family=Poppins:wght@400;500;600;700&family=Oswald:wght@500;600&family=Jost:wght@400;500&family=Monsieur+La+Doulaise&display=swap" rel="stylesheet">
<style>
:root{
  --green:#8dbb3c;
  --green-soft:#f6f9ec;
  --dark:#13301d;
  --footer:#122a1a;
  --ink:#1d1d1d;
  --muted:#555;
  --line:#e3e3e3;
  --blue:#2ba3df;
}
*{box-sizing:border-box;margin:0;padding:0}
html,body{width:1200px;height:4894px;overflow:hidden;background:#fff}
body{font-family:"Poppins",sans-serif;color:var(--ink);position:relative}
.abs{position:absolute}
.script{font-family:"Monsieur La Doulaise",cursive;font-weight:400;color:var(--ink);line-height:1}
.heading{font-weight:500;text-transform:uppercase;line-height:1.1}
.heading em{font-style:normal;color:var(--green);font-weight:600}
.swash{position:absolute}
.btn{position:absolute;display:flex;align-items:center;justify-content:space-between;background:var(--green);color:var(--dark);border-radius:30px;font-size:12px;font-weight:500;text-transform:uppercase;padding:0 4px 0 16px}
.btn .go{width:34px;height:34px;border-radius:50%;background:var(--dark);display:flex;align-items:center;justify-content:center}
.circle-arrow{display:flex;align-items:center;justify-content:center;border-radius:50%}

.site-header{top:0;left:0;width:1200px;height:95px;background:#fff}
.brand{left:142px;top:24px;display:flex;align-items:center;gap:10px}
.brand-mark{width:42px;height:42px;border-radius:50%;background:var(--dark)}
.brand-name{font-size:12px;font-weight:600;color:var(--dark);text-transform:uppercase}
.nav{left:550px;top:38px;display:flex;gap:22px;font-size:13px;text-transform:uppercase}

.hero{top:95px;left:0;width:1200px;height:580px;background:linear-gradient(90deg,#2b3022 0%,#4b4d3c 35%,#7c8068 60%,#a9a88f 80%,#6f7d4a 100%)}
.hero-tag{left:139px;top:236px;background:var(--green);color:var(--dark);font-family:"Oswald",sans-serif;font-size:12px;padding:3px 8px;text-transform:uppercase}
.hero-title{left:139px;top:262px;font-family:"Oswald",sans-serif;font-weight:500;font-size:46px;line-height:49px;color:#fff;text-transform:uppercase}
.hero-title em{font-style:normal;color:var(--green)}

.about-text{left:142px;top:958px;width:410px;font-size:12.5px;line-height:24px;color:#222}
.photo{position:absolute;box-shadow:0 12px 30px rgba(0,0,0,.18)}

.prop{top:1501px;width:288px;height:342px;overflow:hidden}
.prop-label{position:absolute;left:21px;bottom:26px;color:#fff}
.prop-label small{display:block;font-size:11px}
.prop-label b{font-weight:500;font-size:14px}
.prop .circle-arrow{position:absolute;right:15px;bottom:20px;width:42px;height:42px;border:1.5px solid #fff}

.service{top:2090px;width:281px;height:310px;background:#fff;box-shadow:0 6px 26px rgba(0,0,0,.09);text-align:center}
.service-icon{position:absolute;left:50%;top:-36px;width:110px;height:110px;margin-left:-55px;border-radius:50%}
.service h3{margin-top:100px;font-size:20px;font-weight:700;line-height:25px;text-transform:uppercase;color:#1a1a1a}
.service p{margin:14px auto 0;width:240px;font-size:12.5px;line-height:23px;color:var(--muted)}
.service .circle-arrow{position:absolute;left:50%;bottom:-18px;width:42px;height:42px;margin-left:-21px}

.rates{top:2500px;left:0;width:1200px;height:783px;background:var(--green-soft)}
.chart-card{left:346px;top:2742px;width:509px;height:380px;background:#fff;border-top:4px solid var(--blue)}
.chart-card h4{position:absolute;left:20px;top:18px;font-size:16.5px;font-weight:700;line-height:21px;color:#1a2a3a}

.review{top:3545px;width:342px;height:241px;background:#fff;box-shadow:0 4px 20px rgba(0,0,0,.08);overflow:hidden}
.avatar{position:absolute;left:16px;top:23px;width:46px;height:46px;border-radius:50%;background:linear-gradient(135deg,#b79a82,#5e4a3e)}
.review .name{position:absolute;left:76px;top:27px;font-family:"Jost",sans-serif;font-size:14px;color:#222}
.review .date{position:absolute;left:76px;top:48px;font-family:"Jost",sans-serif;font-size:12px;color:#aaa}
.review .stars{position:absolute;right:18px;top:33px;color:#f2b705;font-size:14px;letter-spacing:1px}
.review p{position:absolute;left:16px;top:104px;width:300px;font-family:"Jost",sans-serif;font-size:12.5px;line-height:21.5px;color:#333}
.review .quote{position:absolute;right:14px;bottom:-46px;font-family:"Poppins",sans-serif;font-weight:700;font-size:130px;color:#cfcfcf;line-height:1}
.arrow-btn{top:3450px;width:38px;height:38px;border:1px solid #bbb;background:#fff}

.field{position:absolute;border:1px solid var(--line);border-radius:3px;display:flex;align-items:center;font-size:11.5px;color:#888}
.field svg{margin:0 12px 0 14px}
.field .sep{width:1px;height:20px;background:var(--line);margin-right:12px}
.submit{left:547px;top:4343px;width:511px;height:52px;background:var(--green);color:#fff;font-size:12px;font-weight:600;display:flex;align-items:center;justify-content:center;text-transform:uppercase;border-radius:2px}

.site-footer{top:4526px;left:0;width:1200px;height:368px;background:var(--footer);color:#fff}
.site-footer h5{font-size:13px;font-weight:500;text-transform:uppercase;letter-spacing:.5px}
.site-footer ul{list-style:none;font-size:12.5px;line-height:28px}
.contact-list{font-size:12px;line-height:18px}
.contact-item{display:flex;gap:8px;margin-bottom:12px}
.social li{display:flex;align-items:center;gap:10px;margin-bottom:11px;line-height:30px}
.social .dot{width:30px;height:30px;border-radius:50%;border:1px solid #fff}
.social .dot.on{background:var(--green);border-color:var(--green)}
.copyright{left:0;top:4858px;width:1200px;text-align:center;font-size:12px;color:#fff}
</style>
</head>
<body>

<header class="abs site-header">
  <div class="abs brand">
    <span class="brand-mark"></span>
    <span class="brand-name">Beacon Lending and Capital</span>
  </div>
  <nav class="abs nav">
    <span>Home</span><span>About Us</span><span>Properties</span><span>Contact Us</span>
  </nav>
  <div class="btn" style="left:884px;top:26px;width:175px;height:44px">Customer Login<span class="go"><svg width="14" height="14" viewBox="0 0 14 14"><path d="M3 11 11 3M5 3h6v6" stroke="#fff" stroke-width="1.6" fill="none"/></svg></span></div>
</header>

<section class="abs hero" role="img" aria-label="Family of four standing in front of a suburban home with a green lawn"></section>
<div class="abs hero-tag">Residential Home Loans in Florida and Commercial Lending in America</div>
<h1 class="abs hero-title">Your Best Resource<br>For Hassle-Free,<br><em>Low Cost Mortgage</em><br>Origination</h1>
<div class="btn" style="left:139px;top:496px;width:147px;height:42px">Apply Now<span class="go"><svg width="14" height="14" viewBox="0 0 14 14"><path d="M3 11 11 3M5 3h6v6" stroke="#fff" stroke-width="1.6" fill="none"/></svg></span></div>

<div class="abs script" style="left:150px;top:752px;font-size:96px">About</div>
<h2 class="abs heading" style="left:139px;top:843px;font-size:32px;font-weight:400">Beacon<br><em style="font-size:33px">Lending &amp; Capital</em></h2>
<p class="abs about-text">Beacon Lending Originates Residential Home Loans In Florida And Commercial And Business Financing In All 50 States. We Have Over 25 Years Of Experience In ALL Types Of Real Estate And Commercial Lending. We Are Strategically Partnered To Help You Obtain ALL Necessary Components Of Residential And Commercial Lending. From The RIGHT Lending Partners To The Best Practice Insurance Avenues And Commercial And Residential Real Estate Partners</p>
<div class="btn" style="left:142px;top:1179px;width:150px;height:42px">Read More<span class="go"><svg width="14" height="14" viewBox="0 0 14 14"><path d="M3 11 11 3M5 3h6v6" stroke="#fff" stroke-width="1.6" fill="none"/></svg></span></div>
<div class="photo" style="left:667px;top:766px;width:389px;height:391px;background:linear-gradient(135deg,#3c3f44,#8a8f96 50%,#c8c5c0)" role="img" aria-label="Advisors reviewing mortgage documents with a couple"></div>
<div class="photo" style="left:592px;top:1003px;width:240px;height:260px;background:linear-gradient(160deg,#7fa0b8,#c9b08a 60%,#8a6a3c)" role="img" aria-label="Small model house on stacks of coins"></div>

<div class="abs script" style="left:470px;top:1320px;font-size:92px">Properties</div>
<h2 class="abs heading" style="left:0;width:1200px;text-align:center;top:1408px;font-size:36px;font-weight:400">Available <em>Properties</em></h2>
<svg class="swash" style="left:520px;top:1452px" width="170" height="12"><path d="M2 9 Q85 1 168 6" stroke="var(--green)" stroke-width="2" fill="none"/></svg>

<div class="abs prop" style="left:0" role="img" aria-label="Modern white house exterior">
  <div style="position:absolute;inset:0;background:linear-gradient(180deg,#d8d8d8,#9a9a9a 60%,#2b2b2b)"></div>
  <div class="prop-label"><small>12 Property</small><b>Sunset Street</b></div>
  <span class="circle-arrow"><svg width="14" height="14"><path d="M3 11 11 3M5 3h6v6" stroke="#fff" stroke-width="1.5" fill="none"/></svg></span>
</div>
<div class="abs prop" style="left:304px" role="img" aria-label="Dark modern building at dusk">
  <div style="position:absolute;inset:0;background:linear-gradient(180deg,#5a7da3,#1d2633 55%,#6a4a2a)"></div>
  <div class="prop-label"><small>24 Property</small><b>Union Avenue</b></div>
  <span class="circle-arrow"><svg width="14" height="14"><path d="M3 11 11 3M5 3h6v6" stroke="#fff" stroke-width="1.5" fill="none"/></svg></span>
</div>
<div class="abs prop" style="left:608px" role="img" aria-label="City street lined with tall apartment towers">
  <div style="position:absolute;inset:0;background:linear-gradient(180deg,#9aa2a8,#6b5a4e 55%,#2e2a28)"></div>
  <div class="prop-label"><small>56 Property</small><b>Washington Street</b></div>
  <span class="circle-arrow"><svg width="14" height="14"><path d="M3 11 11 3M5 3h6v6" stroke="#fff" stroke-width="1.5" fill="none"/></svg></span>
</div>
<div class="abs prop" style="left:913px" role="img" aria-label="Brick and glass office facade">
  <div style="position:absolute;inset:0;background:linear-gradient(90deg,#8a3e2e,#5a4a4a 50%,#5d89b5)"></div>
  <div class="prop-label"><small>78 Property</small><b>Oak Boulevard</b></div>
  <span class="circle-arrow"><svg width="14" height="14"><path d="M3 11 11 3M5 3h6v6" stroke="#fff" stroke-width="1.5" fill="none"/></svg></span>
</div>

<div class="abs script" style="left:495px;top:1880px;font-size:92px">Services</div>
<h2 class="abs heading" style="left:0;width:1200px;text-align:center;top:1960px;font-size:36px;font-weight:400">Our <em>Services</em></h2>
<svg class="swash" style="left:490px;top:2003px" width="220" height="12"><path d="M2 9 Q110 1 218 6" stroke="var(--green)" stroke-width="2" fill="none"/></svg>

<div class="abs service" style="left:144px">
  <div class="service-icon" style="background:var(--green)"><svg width="110" height="110" viewBox="0 0 110 110"><path d="M30 55 55 33 80 55M38 50v25h34V50M50 75V62h10v13" stroke="#fff" stroke-width="4" fill="none" stroke-linejoin="round"/></svg></div>
  <h3>Residential<br>Loan</h3>
  <p>Lorem Ipsum is simply dummy text of the printing and typesett industry. Lorem Ipsum has been the industry's standard</p>
  <span class="circle-arrow" style="background:var(--dark)"><svg width="14" height="14"><path d="M3 11 11 3M5 3h6v6" stroke="#fff" stroke-width="1.5" fill="none"/></svg></span>
</div>
<div class="abs service" style="left:459px">
  <div class="service-icon" style="background:var(--dark)"><svg width="110" height="110" viewBox="0 0 110 110"><path d="M40 80V34h30v46M34 80h42M47 42h5M58 42h5M47 52h5M58 52h5M47 62h5M58 62h5M51 80v-9h8v9" stroke="#fff" stroke-width="3.5" fill="none"/></svg></div>
  <h3>Commercial<br>Loan</h3>
  <p>Lorem Ipsum is simply dummy text of the printing and typesett industry. Lorem Ipsum has been the industry's standard</p>
  <span class="circle-arrow" style="background:var(--green)"><svg width="14" height="14"><path d="M3 11 11 3M5 3h6v6" stroke="#fff" stroke-width="1.5" fill="none"/></svg></span>
</div>
<div class="abs service" style="left:776px">
  <div class="service-icon" style="background:var(--green)"><svg width="110" height="110" viewBox="0 0 110 110"><path d="M38 52 55 37 72 52M43 48v16h24V48" stroke="#fff" stroke-width="3.5" fill="none"/><circle cx="55" cy="55" r="5" stroke="#fff" stroke-width="3" fill="none"/><path d="M28 70q10-4 22 2l14 1q6 2 0 6H50M28 80q16 6 26 4l22-10" stroke="#fff" stroke-width="3.5" fill="none" stroke-linecap="round"/></svg></div>
  <h3>Property<br>Mortgage</h3>
  <p>Lorem Ipsum is simply dummy text of the printing and typesett industry. Lorem Ipsum has been the industry's standard</p>
  <span class="circle-arrow" style="background:var(--dark)"><svg width="14" height="14"><path d="M3 11 11 3M5 3h6v6" stroke="#fff" stroke-width="1.5" fill="none"/></svg></span>
</div>

<section class="abs rates"></section>
<div class="abs script" style="left:480px;top:2570px;font-size:92px">Mortgage</div>
<h2 class="abs heading" style="left:0;width:1200px;text-align:center;top:2652px;font-size:36px;font-weight:400">Mortgage <em>Rate Chart</em></h2>
<svg class="swash" style="left:560px;top:2695px" width="250" height="12"><path d="M2 9 Q125 1 248 6" stroke="var(--green)" stroke-width="2" fill="none"/></svg>

<div class="abs chart-card">
  <h4>General Mortgage Rate Trends by Loan Term<br>Illustrative Yearly Averages, Not a Rate Quote</h4>
  <svg style="position:absolute;left:0;top:60px" width="509" height="316" viewBox="0 0 509 316" font-family="Poppins, sans-serif" font-size="8" fill="#666">
    <g stroke="#eee" stroke-width="1">
      <line x1="36" y1="30" x2="490" y2="30"/><line x1="36" y1="78" x2="490" y2="78"/><line x1="36" y1="126" x2="490" y2="126"/><line x1="36" y1="174" x2="490" y2="174"/><line x1="36" y1="222" x2="490" y2="222"/>
    </g>
    <line x1="36" y1="270" x2="490" y2="270" stroke="#999"/>
    <text x="24" y="33">10</text><text x="28" y="81">8</text><text x="28" y="129">6</text><text x="28" y="177">4</text><text x="28" y="225">2</text><text x="28" y="273">0</text>
    <text x="34" y="284">2015</text><text x="120" y="284">2017</text><text x="206" y="284">2019</text><text x="292" y="284">2021</text><text x="378" y="284">2023</text><text x="466" y="284">2025</text>
    <text x="375" y="298" font-size="6.5" fill="#999">Beacon internal averages</text>
    <polyline fill="none" stroke="#7cc242" stroke-width="2" points="36,174 79,170 122,165 165,150 208,172 251,196 294,192 337,132 380,98 423,104 466,116 490,120"/>
    <polyline fill="none" stroke="#2ba3df" stroke-width="2" points="36,192 79,189 122,184 165,170 208,190 251,212 294,208 337,150 380,116 423,124 466,136 490,140"/>
    <g fill="#7cc242"><circle cx="380" cy="98" r="3"/><circle cx="251" cy="196" r="3"/></g>
    <g fill="#2ba3df"><circle cx="380" cy="116" r="3"/><circle cx="251" cy="212" r="3"/></g>
    <line x1="48" y1="22" x2="62" y2="22" stroke="#7cc242" stroke-width="2"/><text x="66" y="25">30-Year Fixed</text>
    <line x1="140" y1="22" x2="154" y2="22" stroke="#2ba3df" stroke-width="2"/><text x="158" y="25">15-Year Fixed</text>
  </svg>
</div>
<div class="btn" style="left:513px;top:3161px;width:173px;height:40px">Customer Login<span class="go"><svg width="14" height="14" viewBox="0 0 14 14"><path d="M3 11 11 3M5 3h6v6" stroke="#fff" stroke-width="1.6" fill="none"/></svg></span></div>

<div class="abs script" style="left:150px;top:3365px;font-size:92px">Testimonial</div>
<h2 class="abs heading" style="left:145px;top:3446px;font-size:36px;font-weight:400">Reviews From <em>Customers</em></h2>
<svg class="swash" style="left:430px;top:3490px" width="250" height="12"><path d="M2 9 Q125 1 248 6" stroke="var(--green)" stroke-width="2" fill="none"/></svg>
<span class="abs arrow-btn circle-arrow" style="left:969px"><svg width="12" height="12"><path d="M8 2 4 6l4 4" stroke="#555" stroke-width="1.4" fill="none"/></svg></span>
<span class="abs arrow-btn circle-arrow" style="left:1018px"><svg width="12" height="12"><path d="M4 2l4 4-4 4" stroke="#555" stroke-width="1.4" fill="none"/></svg></span>

<div class="abs review" style="left:148px">
  <span class="avatar" role="img" aria-label="Customer portrait"></span>
  <span class="name">Daniel Morrow</span><span class="date">24December 2024</span><span class="stars">★★★★★</span>
  <p>Lorem Ipsum Dolor Sit Amet Consectetur Adipiscing Elit, Sed Do Eiusmod Tempor Incididunt Ut Labore Et Dolore Magna Aliqua. Ut Enim Ad Miim Veniam Quis Nostrud Exercitation Ullamco Laboris Nisi Ut Aliquip Ex Ea Commodo Consequat.</p>
  <span class="quote">”</span>
</div>
<div class="abs review" style="left:532px">
  <span class="avatar" role="img" aria-label="Customer portrait"></span>
  <span class="name">Jonah Albright</span><span class="date">24December 2024</span><span class="stars">★★★★★</span>
  <p>Lorem Ipsum Dolor Sit Amet Consectetur Adipiscing Elit, Sed Do Eiusmod Tempor Incididunt Ut Labore Et Dolore Magna Aliqua. Ut Enim Ad Miim Veniam Quis Nostrud Exercitation Ullamco Laboris Nisi Ut Aliquip Ex Ea Commodo Consequat.</p>
  <span class="quote">”</span>
</div>
<div class="abs review" style="left:916px">
  <span class="avatar" role="img" aria-label="Customer portrait"></span>
  <span class="name">Marcus Jensen</span><span class="date">24December 2024</span><span class="stars">★★★★★</span>
  <p>Lorem Ipsum Dolor Sit Amet Consectetur Adipiscing Elit, Sed Do Eiusmod Tempor Incididunt Ut Labore Et Dolore Magna Aliqua. Ut Enim Ad Miim Veniam Quis Nostrud Exercitation Ullamco Laboris Nisi Ut Aliquip Ex Ea Commodo Consequat.</p>
  <span class="quote">”</span>
</div>
<div class="abs" style="left:1150px;top:3530px;width:50px;height:270px;background:linear-gradient(90deg,rgba(255,255,255,0),#fff)"></div>

<div class="abs" style="left:140px;top:3914px;width:357px;height:481px;background:linear-gradient(180deg,#c9b9d4 0%,#a7a9c6 30%,#b57a58 65%,#5a4a3e 100%)" role="img" aria-label="Downtown skyline with a tall government tower at dusk"></div>
<div class="abs script" style="left:555px;top:3908px;font-size:92px">Contact</div>
<h2 class="abs heading" style="left:547px;top:3990px;font-size:36px;font-weight:400">Get In <em>Touch</em></h2>
<svg class="swash" style="left:680px;top:4033px" width="150" height="12"><path d="M2 9 Q75 1 148 6" stroke="var(--green)" stroke-width="2" fill="none"/></svg>

<div class="field" style="left:547px;top:4075px;width:245px;height:53px"><svg width="14" height="14"><circle cx="7" cy="5" r="3" stroke="#999" fill="none"/><path d="M1 13q6-7 12 0" stroke="#999" fill="none"/></svg><span class="sep"></span>First Name</div>
<div class="field" style="left:812px;top:4075px;width:246px;height:53px"><svg width="14" height="14"><circle cx="7" cy="5" r="3" stroke="#999" fill="none"/><path d="M1 13q6-7 12 0" stroke="#999" fill="none"/></svg><span class="sep"></span>Last Name</div>
<div class="field" style="left:547px;top:4143px;width:245px;height:53px"><svg width="14" height="14"><rect x="1" y="3" width="12" height="9" stroke="#999" fill="none"/><path d="M1 3l6 5 6-5" stroke="#999" fill="none"/></svg><span class="sep"></span>Your Email</div>
<div class="field" style="left:812px;top:4143px;width:246px;height:53px"><svg width="14" height="14"><path d="M3 1l3 3-2 2q2 4 4 4l2-2 3 3-2 2Q3 12 1 3z" stroke="#999" fill="none"/></svg><span class="sep"></span>Phone</div>
<div class="field" style="left:547px;top:4210px;width:511px;height:108px;align-items:flex-start;padding-top:18px"><svg width="14" height="14"><rect x="1" y="2" width="12" height="8" rx="2" stroke="#999" fill="none"/><path d="M4 10v3l3-3" stroke="#999" fill="none"/></svg><span class="sep"></span>Your Message</div>
<div class="abs submit">Submit Now</div>

<footer class="abs site-footer">
  <div class="abs" style="left:142px;top:120px;display:flex;align-items:center;gap:10px">
    <span style="width:40px;height:40px;border-radius:50%;background:#fff"></span>
    <span style="font-size:14px;font-weight:600;line-height:18px">Beacon Lending<br>and Capital</span>
  </div>
  <div class="abs" style="left:397px;top:70px">
    <h5>Quick Links</h5>
    <ul style="margin-top:8px"><li>Home</li><li>About Us</li><li>Properties</li><li>Contact Us</li></ul>
  </div>
  <div class="abs contact-list" style="left:612px;top:70px;width:250px">
    <h5 style="margin-bottom:14px">Contact Details</h5>
    <div class="contact-item"><svg width="12" height="14"><path d="M6 13S1 7.5 1 5a5 5 0 0110 0c0 2.5-5 8-5 8z" fill="#fff"/><circle cx="6" cy="5" r="2" fill="var(--footer)"/></svg><span>200 Harbor Point Drive<br>Gulfport Bay, FL</span></div>
    <div class="contact-item"><svg width="12" height="12"><path d="M2 0l3 3-1.5 1.5q1.5 3 4 4L9 7l3 3-2 2Q1 10 0 2z" fill="#fff"/></svg><span>Phone<br>+123 555 0142</span></div>
    <div class="contact-item"><svg width="12" height="12"><rect x="0" y="2" width="12" height="8" fill="#fff"/><path d="M0 2l6 5 6-5" stroke="var(--footer)" fill="none"/></svg><span>Email<br><span style="font-size:10.5px">info@beaconlendingandcapital.example</span></span></div>
  </div>
  <div class="abs" style="left:953px;top:70px">
    <h5>Social Media</h5>
    <ul class="social" style="margin-top:14px">
      <li><span class="dot on"></span>Community Page</li>
      <li><span class="dot"></span>Video Channel</li>
      <li><span class="dot"></span>Pro Network</li>
      <li><span class="dot"></span>Photo Feed</li>
    </ul>
  </div>
  <div class="abs" style="left:0;top:318px;width:1200px;height:1px;background:rgba(255,255,255,.15)"></div>
</footer>
<div class="abs copyright">© 2025 Beacon Lending And Capital. All Rights Reserved.</div>

</body>
</html>
```